Harborline Talent IT Recruiting firm needs a business card design for Recruiters, Sourcers, and Account

We need business cards that allow us to change all contact info, names, titles (Recruiter, Sourcer, Account Manager, Director, CEO, etc) per person since we have three offices, in three cities, Phoenix, Austin, and Las Vegas. We do recruiting and contractors for IT positions (Developers, Architects, Software Engineers, Security Engineers, Help Desk, DBAs, PMs, Scrum Masters, etc.) Our client companies are very diverse from Crestline 250 to silicone Valley type start-ups.

So, while we what hip, techie, and quirky, it still needs to be professional. Primary color we use is blue, with silver as a secondary color.

Target Market(s)

IT, Technology

Industry/Entity Type

Business

Contact Information for Business Card

Company name: Harborline Talent, Inc.
Website: www.harborlinetalent-example.com
Logos for ProCircle, Quillo, and Roomwall

Name, Title, Office Number, Cell Number, email

Font styles to use
Serif
Sans Serif

Colors
0455a3
d5d5d5

Requirements
Nice to have
• The grey I selected below is not necessary - but, would like silver included. I included a card design (File 3: HTI early trial example.jpg) that I had started on. It's very rough, and not quite what we're looking for, but what we did like is the logo, big, maybe a bit faded, off center, goes out of frame, etc. Still looking for other ideas - you are the pros! But, just an idea of a design element we liked.

```html
<!DOCTYPE html>
<html lang="en">
<head>
<meta charset="utf-8">
<title>Harborline Talent – Business Card</title>
<link href="https://fonts.googleapis.com/css2?family=Lato:wght@300;400;700&family=Cinzel:wght@400&display=swap" rel="stylesheet">
<style>
  :root {
    --brand-blue: #0455a3;
    --brand-blue-deep: #0a4a94;
    --brand-blue-light: #2f7fd0;
    --sky: #3aa0dc;
    --silver: #d5d5d5;
    --ink-grey: #6b6f75;
    --paper: #ffffff;
    --backdrop: #ecebe8;
  }
  * { margin: 0; padding: 0; box-sizing: border-box; }
  html, body {
    width: 1200px; height: 1023px; overflow: hidden;
    background: var(--backdrop);
    font-family: "Lato", Arial, sans-serif;
  }
  .stage { position: relative; width: 1200px; height: 1023px; }

  .card {
    position: absolute; width: 560px; height: 320px;
    border-radius: 4px; overflow: hidden;
    box-shadow: 0 6px 18px rgba(0,0,0,.18);
  }

  /* Brand block (shared) */
  .brand { display: inline-block; }
  .brand-name {
    display: flex; align-items: center; gap: 10px;
    font-weight: 300; font-size: 30px; letter-spacing: 3px;
    color: var(--brand-blue); text-transform: uppercase; line-height: 1;
    white-space: nowrap;
  }
  .brand-dot { flex: none; width: 26px; height: 26px; border-radius: 50%; background: var(--brand-blue-light); }
  .tagline {
    margin-top: 10px;
    font-family: "Cinzel", Georgia, serif; font-size: 10px; letter-spacing: 2.4px;
    color: var(--ink-grey); text-transform: uppercase; white-space: nowrap;
  }

  /* Front */
  .card-front { left: 60px; top: 120px; background: var(--paper); }
  .front-mark {
    position: absolute; right: -70px; top: -90px; width: 320px; height: 320px;
    border-radius: 50%;
    background: radial-gradient(circle, rgba(4,85,163,.09) 0%, rgba(4,85,163,.05) 55%, rgba(4,85,163,0) 72%);
  }
  .front-brand { position: absolute; left: 34px; top: 42px; }
  .front-brand .tagline { margin-left: 36px; }
  .person { position: absolute; left: 34px; top: 122px; }
  .person-name { font-weight: 700; font-size: 19px; color: var(--brand-blue); }
  .person-title { font-size: 15px; color: var(--brand-blue); margin-top: 1px; }
  .contacts { position: absolute; left: 34px; top: 180px; list-style: none; }
  .contacts li {
    display: flex; align-items: center; gap: 10px;
    font-size: 13px; color: var(--ink-grey); line-height: 19px;
  }
  .contacts svg { flex: none; width: 12px; height: 12px; fill: var(--ink-grey); }
  .front-band { position: absolute; left: 0; bottom: 0; width: 560px; height: 90px; }
  .address {
    position: absolute; right: 20px; bottom: 18px;
    color: var(--paper); font-size: 15px; letter-spacing: .3px; white-space: nowrap;
  }

  /* Back */
  .card-back {
    left: 580px; top: 560px;
    background: linear-gradient(160deg, var(--brand-blue-light) 0%, var(--brand-blue) 45%, var(--brand-blue-deep) 100%);
  }
  .back-brand { position: absolute; left: 0; right: 0; top: 112px; text-align: center; }
  .back-brand .brand-name { justify-content: center; color: var(--paper); font-size: 36px; }
  .back-brand .brand-dot { width: 30px; height: 30px; background: var(--paper); }
  .back-brand .tagline { margin-top: 14px; color: var(--silver); font-size: 11px; }
  .social { position: absolute; left: 22px; bottom: 18px; list-style: none; display: flex; gap: 14px; }
  .social li { font-size: 11px; color: var(--paper); letter-spacing: .5px; }
</style>
</head>
<body>
<main class="stage">

  <section class="card card-front" aria-label="Business card front">
    <div class="front-mark" role="img" aria-label="Faint oversized brand mark area"></div>

    <div class="brand front-brand">
      <div class="brand-name"><span class="brand-dot"></span>Harborline Talent</div>
      <p class="tagline">Charting What Comes Next</p>
    </div>

    <div class="person">
      <p class="person-name">Maren Ellison</p>
      <p class="person-title">CEO</p>
    </div>

    <ul class="contacts">
      <li><svg viewBox="0 0 12 12"><path d="M2 1h2l1 3-1.5 1a7 7 0 0 0 3.5 3.5L8 7l3 1v2a1 1 0 0 1-1 1A9 9 0 0 1 1 2a1 1 0 0 1 1-1z"/></svg>(602) 555-0148</li>
      <li><svg viewBox="0 0 12 12"><rect x="3" y="0.5" width="6" height="11" rx="1"/></svg>(602) 555-0193</li>
      <li><svg viewBox="0 0 12 12"><path d="M0 2h12v8H0z M0 2l6 4 6-4"/></svg>maren@harborlinetalent-example.com</li>
      <li><svg viewBox="0 0 12 12"><path d="M1 1h10v8H1z M4 11h4v-1H4z"/></svg>www.harborlinetalent-example.com</li>
    </ul>

    <svg class="front-band" viewBox="0 0 560 90" preserveAspectRatio="none" aria-hidden="true">
      <path d="M0 62 L110 62 Q130 62 150 46 L560 30 L560 90 L0 90 Z" fill="var(--sky)" opacity=".55"/>
      <path d="M0 70 L110 70 Q132 70 150 54 L560 40 L560 90 L0 90 Z" fill="var(--brand-blue)"/>
    </svg>
    <p class="address">2140 E Larkspur Ave, Suite 310 Phoenix, AZ 85099, USA</p>
  </section>

  <section class="card card-back" aria-label="Business card back">
    <div class="back-brand">
      <div class="brand-name"><span class="brand-dot"></span>Harborline Talent</div>
      <p class="tagline">Charting What Comes Next</p>
    </div>
    <ul class="social">
      <li>Roomwall</li>
      <li>Quillo</li>
      <li>ProCircle</li>
    </ul>
  </section>

</main>
</body>
</html>
```